Marrowfield Contracting Business Cards

Front of card:

Full Logo
Name
Address
Office Phone
Cell Phone
Email
Website

Back:
Logo Mark in background
List and markets and services performed

```html
<!DOCTYPE html>
<html lang="en">
<head>
<meta charset="UTF-8">
<title>Marrowfield Contracting Business Cards</title>
<link href="https://fonts.googleapis.com/css2?family=Montserrat:wght@400;500;700&display=swap" rel="stylesheet">
<style>
  :root {
    --brand-red: #d61f1f;
    --brand-grey: #7d7d7d;
    --paper-white: #ffffff;
    --ink-white: #ffffff;
    --canvas-bg: #e9e9e9;
  }
  * { margin: 0; padding: 0; box-sizing: border-box; }
  html, body {
    width: 1200px;
    height: 1200px;
    overflow: hidden;
    background: var(--canvas-bg);
    font-family: "Montserrat", Arial, sans-serif;
  }
  .sheet { position: relative; width: 1200px; height: 1200px; }
  .card {
    position: absolute;
    left: 150px;
    width: 900px;
    height: 514px;
    border-radius: 40px;
    overflow: hidden;
    box-shadow: 0 10px 30px rgba(0,0,0,0.18);
  }
  .card--front { top: 60px; }
  .card--back { top: 626px; background: var(--brand-red); }
  .card-bg { position: absolute; inset: 0; width: 100%; height: 100%; }

  .wordmark {
    position: absolute;
    display: flex;
    flex-direction: column;
    align-items: center;
    text-align: center;
    font-weight: 700;
    letter-spacing: 0.06em;
    text-transform: uppercase;
    line-height: 1.1;
  }
  .wordmark__dot { flex: none; border-radius: 50%; }
  .wordmark__llc { display: block; letter-spacing: 0.3em; margin-top: 6px; }
  .wordmark__rule { display: block; height: 2px; margin-top: 10px; }

  .wordmark--front {
    left: 60px;
    width: 380px;
    top: 130px;
    gap: 20px;
    color: var(--brand-red);
    font-size: 30px;
  }
  .wordmark--front .wordmark__dot { width: 96px; height: 96px; background: var(--brand-red); }
  .wordmark--front .wordmark__llc { font-size: 15px; }
  .wordmark--front .wordmark__rule { width: 260px; background: var(--brand-grey); }

  .contact {
    position: absolute;
    left: 560px;
    top: 110px;
    color: var(--ink-white);
  }
  .contact__name { font-size: 38px; font-weight: 700; letter-spacing: 0.01em; line-height: 1.15; }
  .contact__role { font-size: 22px; font-weight: 400; letter-spacing: 0.05em; margin-bottom: 20px; }
  .contact__list { list-style: none; }
  .contact__item {
    display: flex;
    align-items: center;
    gap: 12px;
    font-size: 18px;
    font-weight: 500;
    margin-bottom: 9px;
    line-height: 1.25;
  }
  .contact__item svg { width: 20px; height: 20px; flex: none; }
  .contact__label { font-weight: 700; }

  .wordmark--back {
    left: 0;
    right: 0;
    top: 64px;
    gap: 20px;
    color: var(--ink-white);
    font-size: 40px;
  }
  .wordmark--back .wordmark__dot { width: 100px; height: 100px; background: var(--ink-white); }
  .wordmark--back .wordmark__llc { font-size: 18px; }
  .wordmark--back .wordmark__rule { width: 360px; margin: 12px auto 0; background: var(--ink-white); }

  .services {
    position: absolute;
    left: 60px;
    right: 60px;
    top: 400px;
    color: var(--ink-white);
    text-align: center;
  }
  .services__heading {
    font-size: 15px;
    font-weight: 700;
    letter-spacing: 0.25em;
    text-transform: uppercase;
    margin-bottom: 10px;
  }
  .services__list {
    list-style: none;
    display: flex;
    justify-content: center;
    flex-wrap: wrap;
    gap: 6px 0;
    font-size: 17px;
    font-weight: 500;
  }
  .services__list li + li::before { content: "•"; margin: 0 12px; }
</style>
</head>
<body>
<main class="sheet">

  <section class="card card--front" aria-label="Business card front">
    <svg class="card-bg" viewBox="0 0 900 514" preserveAspectRatio="none" aria-hidden="true">
      <rect width="900" height="514" fill="var(--brand-red)"/>
      <path d="M0 0 H300 C480 60 560 300 500 514 H0 Z" fill="var(--paper-white)"/>
      <path d="M306 0 C500 55 590 300 522 514" fill="none" stroke="var(--brand-grey)" stroke-width="14"/>
    </svg>

    <div class="wordmark wordmark--front">
      <span class="wordmark__dot"></span>
      <span>Marrowfield<br>Contracting<span class="wordmark__llc">LLC</span><span class="wordmark__rule"></span></span>
    </div>

    <div class="contact">
      <p class="contact__name">FULL NAME</p>
      <p class="contact__role">POSITION</p>
      <ul class="contact__list">
        <li class="contact__item">
          <svg viewBox="0 0 24 24" fill="var(--ink-white)"><path d="M6.6 10.8a15.1 15.1 0 0 0 6.6 6.6l2.2-2.2c.3-.3.7-.4 1-.2 1.1.4 2.3.6 3.6.6.6 0 1 .4 1 1V20c0 .6-.4 1-1 1A17 17 0 0 1 3 4c0-.6.4-1 1-1h3.5c.6 0 1 .4 1 1 0 1.3.2 2.5.6 3.6.1.3 0 .7-.2 1z"/></svg>
          <span><span class="contact__label">O:</span> (000) 000 0000</span>
        </li>
        <li class="contact__item">
          <svg viewBox="0 0 24 24" fill="none" stroke="var(--ink-white)" stroke-width="2"><rect x="6" y="2" width="12" height="20" rx="2"/><path d="M10 18h4"/></svg>
          <span><span class="contact__label">C:</span> (000) 000 0000</span>
        </li>
        <li class="contact__item">
          <svg viewBox="0 0 24 24"><path d="M2 5h20v14H2z" fill="none" stroke="var(--ink-white)" stroke-width="2"/><path d="M2 5l10 8 10-8" fill="none" stroke="var(--ink-white)" stroke-width="2"/></svg>
          email@company.com
        </li>
        <li class="contact__item">
          <svg viewBox="0 0 24 24" fill="none" stroke="var(--ink-white)" stroke-width="1.8"><circle cx="12" cy="12" r="9.5"/><ellipse cx="12" cy="12" rx="4" ry="9.5"/><path d="M2.5 12h19M4 7h16M4 17h16"/></svg>
          www.company.com
        </li>
        <li class="contact__item">
          <svg viewBox="0 0 24 24" fill="var(--ink-white)"><path d="M12 2a7 7 0 0 0-7 7c0 5 7 13 7 13s7-8 7-13a7 7 0 0 0-7-7zm0 9.5A2.5 2.5 0 1 1 12 6.5a2.5 2.5 0 0 1 0 5z"/></svg>
          <span>123 Name Street, 000<br>Your City, 00000-000</span>
        </li>
      </ul>
    </div>
  </section>

  <section class="card card--back" aria-label="Business card back">
    <div class="wordmark wordmark--back">
      <span class="wordmark__dot"></span>
      <span>Marrowfield<br>Contracting<span class="wordmark__llc">LLC</span><span class="wordmark__rule"></span></span>
    </div>

    <div class="services">
      <p class="services__heading">Markets &amp; Services</p>
      <ul class="services__list">
        <li>Commercial</li>
        <li>Residential</li>
        <li>Remodeling</li>
        <li>Concrete</li>
        <li>Roofing</li>
        <li>Site Work</li>
      </ul>
    </div>
  </section>

</main>
</body>
</html>
```